AUSTRALIAN CONSULTING FIRM BUSINESS CARD - MODERN

We are wanting a modern, clean lined business card design. We are professional niche consultancy firm situated in Australia called Marlow Advisory Partners Pty Ltd.
The card should communicate professionalism and creativity and draw on our logo design (attached).
The design should be two sided, landscape orientation.
Target Market(s)
government, not for profit sector, corporate clients
Industry/Entity Type
Landscape
Requirements
Must have
- logo
no new introduced colours

```html
<!DOCTYPE html>
<html lang="en">
<head>
<meta charset="utf-8">
<title>Marlow Advisory Partners – Business Card</title>
<link rel="stylesheet" href="https://fonts.googleapis.com/css2?family=Open+Sans:wght@400;600;700&display=swap">
<style>
  :root {
    --stage: #d6d6d6;
    --purple: #612a7c;
    --magenta: #9b2a8e;
    --blue: #1e3f9a;
    --ink: #1c1c1c;
    --paper: #ffffff;
    --faint: #e6e6e6;
    --divider: #bdbdbd;
  }
  * { margin: 0; padding: 0; box-sizing: border-box; }
  html, body { width: 1200px; height: 867px; overflow: hidden; }
  body {
    background: var(--stage);
    font-family: "Open Sans", Arial, sans-serif;
    position: relative;
  }
  .card {
    position: absolute;
    left: 270px;
    width: 660px;
    height: 377px;
    overflow: hidden;
    box-shadow: 0 4px 14px rgba(0,0,0,0.18);
  }
  .card--back { top: 41px; background: var(--purple); color: var(--paper); }
  .card--front { top: 449px; background: var(--paper); }

  .contact-grid {
    position: absolute;
    left: 44px;
    right: 24px;
    bottom: 40px;
    display: grid;
    grid-template-columns: 150px 236px 1fr;
    column-gap: 20px;
    row-gap: 10px;
    font-size: 13px;
    letter-spacing: 0.2px;
  }
  .contact-item { display: flex; align-items: center; gap: 12px; white-space: nowrap; min-width: 0; }
  .contact-item svg { width: 12px; height: 12px; flex: none; fill: var(--paper); }

  .decor-ring {
    position: absolute;
    right: -170px;
    top: 40px;
    width: 420px;
    height: 420px;
    border-radius: 50%;
    border: 46px solid var(--faint);
  }
  .brand {
    position: absolute;
    left: 92px;
    top: 150px;
    display: flex;
    align-items: center;
    gap: 12px;
  }
  .brand-dot { width: 26px; height: 26px; border-radius: 50%; background: var(--blue); flex: none; }
  .brand-name {
    color: var(--blue);
    font-weight: 700;
    font-size: 22px;
    line-height: 1.15;
    letter-spacing: 0.3px;
    max-width: 300px;
  }
  .person {
    position: absolute;
    left: 215px;
    top: 238px;
    display: flex;
    align-items: center;
    gap: 10px;
  }
  .person-name { font-weight: 700; font-size: 17px; color: var(--ink); }
  .person-sep { width: 1px; height: 16px; background: var(--divider); }
  .person-role { font-size: 14px; color: var(--purple); }
</style>
</head>
<body>
  <section class="card card--back" aria-label="Card back">
    <div class="contact-grid">
      <div class="contact-item">
        <svg viewBox="0 0 12 12" aria-hidden="true"><path d="M3 0.5 4.8 3 3.6 4.3c.7 1.6 2 2.9 3.6 3.6L8.5 6.7 11 8.5 10 11c-5 0-9-4-9-9Z"/></svg>
        <span>+61290004127</span>
      </div>
      <div class="contact-item">
        <svg viewBox="0 0 12 12" aria-hidden="true"><path d="M0.5 2h11v8h-11Z M1.8 3.2 6 6.4l4.2-3.2Z" fill-rule="evenodd"/></svg>
        <span>daniel@marlowadvisory.com</span>
      </div>
      <div class="contact-item">
        <svg viewBox="0 0 12 12" aria-hidden="true"><path d="M6 0.8 0.5 5.6h1.6V11h3V7.6h1.8V11h3V5.6h1.6Z"/></svg>
        <span>PO Box 4120</span>
      </div>
      <div class="contact-item">
        <svg viewBox="0 0 12 12" aria-hidden="true"><path d="M3 0h6v12H3Z M4.2 1.3v8.2h3.6V1.3Z" fill-rule="evenodd"/></svg>
        <span>+61412005836</span>
      </div>
      <div class="contact-item">
        <svg viewBox="0 0 12 12" aria-hidden="true"><circle cx="6" cy="6" r="5"/></svg>
        <span>@marlowadvisory</span>
      </div>
    </div>
  </section>

  <section class="card card--front" aria-label="Card front">
    <div class="decor-ring" aria-hidden="true"></div>
    <div class="brand">
      <span class="brand-dot" aria-hidden="true"></span>
      <span class="brand-name">Marlow Advisory Partners Pty Ltd</span>
    </div>
    <div class="person">
      <span class="person-name">Daniel Hart</span>
      <span class="person-sep" aria-hidden="true"></span>
      <span class="person-role">Consultant</span>
    </div>
  </section>
</body>
</html>
```